Vorex Malden Car Wrap

Vehicle: 2025 Vorex Malden (Compact SUV) Style: Luxury, Earthy, Minimalist, Calm Coverage: Full Wrap including the roof (car is silver which does not tie in with the branding)

The Visual Concept: "The Earthy Reset"
Primary Base Color: A deep, matte earthy brown (sampled from the Tidal Housekeep Co. logo). We want to avoid high-gloss "commercial" finishes. A satin finish will give that luxury, high-end feel.

Secondary Accents: Muted cream or "off-white" for text and fine-line details. This creates a high-contrast but "soft" look that feels relaxing rather than aggressive.

Aesthetic Goal: It should look like a mobile spa or a high-end boutique cleaning company. No "bubbles," "sparkles," or typical cleaning icons.

Key Information (The Essentials)
The Tagline: "Your Home, Reset." (Placed elegantly under the side logos or on the rear quarter panels).

Phone Number: 7415 000

Socials/Web: @tidalhousekeepco | tidalhousekeepco.com.au

Somewhere small so not to disrupt the design: A Brennick Group Signature Service maybe with the Brennick Group logo.

Require the print ready and AI files.

```html
<!DOCTYPE html>
<html lang="en">
<head>
<meta charset="utf-8">
<title>Tidal Housekeep Co. — Vorex Malden Wrap, Side Layout</title>
<link rel="stylesheet" href="https://fonts.googleapis.com/css2?family=Poppins:wght@400;500;600&display=swap">
<style>
  :root{
    --canvas:#f0f0f0;
    --wrap-white:#f4f3f1;
    --earth-brown:#5b4a3f;
    --earth-brown-deep:#4c3d33;
    --cream:#d9cfb8;
    --cream-soft:#e8e1d1;
    --trim:#2b2b2b;
  }
  *{margin:0;padding:0;box-sizing:border-box}
  html,body{width:1200px;height:1200px;overflow:hidden;background:var(--canvas)}
  .canvas{position:relative;width:1200px;height:1200px;font-family:"Poppins",sans-serif}
  .wrap-side{position:absolute;left:130px;top:420px;width:940px;height:360px}
  .wrap-side > .panel-art{position:absolute;inset:0;width:100%;height:100%}
  .partner-mark{position:absolute;left:70px;top:62px;display:flex;align-items:center;gap:8px;
    color:var(--cream-soft);font-weight:500;font-size:14px;line-height:1.05}
  .partner-mark .dot{width:18px;height:18px;border-radius:50%;background:var(--cream-soft)}
  .tagline{position:absolute;left:185px;top:118px;color:var(--cream);font-size:23px;line-height:1.35;letter-spacing:.5px}
  .tagline strong{font-weight:600}
  .brand-name{position:absolute;left:425px;top:112px;width:260px;color:var(--earth-brown);text-align:center}
  .brand-name .primary{display:block;font-weight:500;font-size:24px;line-height:1.1;letter-spacing:1.5px;white-space:nowrap}
  .brand-name .secondary{display:block;margin-top:6px;font-weight:400;font-size:11px;letter-spacing:3px}
  .phone{position:absolute;left:418px;top:246px;display:flex;align-items:center;gap:12px;
    color:var(--cream);font-weight:600;font-size:26px;letter-spacing:4px;white-space:nowrap}
  .phone .phone-icon{flex:0 0 24px;width:24px;height:24px}
  .contact-list{position:absolute;left:705px;top:112px;list-style:none;color:var(--trim);font-size:11px;line-height:1.6}
  .contact-list li{display:flex;align-items:center;gap:6px}
  .contact-list .dot{width:9px;height:9px;border-radius:50%;background:var(--earth-brown)}
</style>
</head>
<body>
<main class="canvas">
  <section class="wrap-side" aria-label="Vehicle side wrap layout">
    <svg class="panel-art" viewBox="0 0 940 360" preserveAspectRatio="none" aria-hidden="true">
      <rect class="panel-base" x="0" y="0" width="940" height="360" rx="28" fill="var(--wrap-white)"/>
      <path class="brown-field" d="M28 0 H410 C350 70 380 160 520 195 C600 215 680 222 760 226 L760 360 H28 Q0 360 0 332 V28 Q0 0 28 0 Z" fill="var(--earth-brown)"/>
      <path class="fine-line" d="M410 0 C350 70 380 160 520 195 C600 215 680 222 760 226" fill="none" stroke="var(--cream)" stroke-width="5"/>
      <path class="fine-line" d="M60 118 C110 122 150 140 175 170" fill="none" stroke="var(--cream)" stroke-width="4"/>
      <rect class="sill" x="0" y="332" width="940" height="28" fill="var(--trim)" opacity=".85"/>
    </svg>

    <div class="partner-mark"><span class="dot"></span><span>Brennick<br>Group</span></div>

    <p class="tagline">Your Home,<br><strong>Reset.</strong></p>

    <p class="brand-name">
      <span class="primary">TIDAL HOUSEKEEP</span>
      <span class="secondary">CO.</span>
    </p>

    <p class="phone">
      <svg class="phone-icon" viewBox="0 0 24 24" aria-hidden="true"><circle cx="12" cy="12" r="12" fill="var(--cream)"/><path d="M8.6 6.5l1.6 2.4-1 1.3c.7 1.6 1.9 2.8 3.5 3.5l1.3-1 2.4 1.6-.9 2.2c-4.2-.2-8.8-4.8-9-9z" fill="var(--earth-brown)"/></svg>
      <span>7415 000</span>
    </p>

    <ul class="contact-list">
      <li><span class="dot"></span>@tidalhousekeepco</li>
      <li><span class="dot"></span>tidalhousekeepco.com.au</li>
    </ul>
  </section>
</main>
</body>
</html>
```